Process Roadmap for Interior Design Firm

We are looking to ramp up the design appeal of our current process roadmap to be very visually interesting, while staying informative and descriptive about our process.

Target Market(s)

In-house Clients

Industry/Entity Type

Interior Design Firm focused on sustainable and holistic design.

Other font styles liked:
• raleway

Requirements
Must have
• 1.) it would be nice if the graphic provided a more clear indication of the “journey” from one step to the next, so that there was a clear sense of the progression (such that we are directing the viewer) 2.). We would want it to fit on an 8.5”x11” page (the page could be horizontal when we have the Calm Compass formatted out with the testimonials) (in addition to the testimonials, we may also want to have the detailed descriptions of each step of the process presented below the graphic, so that the graphic is cleaner) 3.) ideally the graphic is clear and simple enough to also be used on our Bi-Weekly Client Updates, which will be typed updates for clients re their project budgets, schedule and scope. The Calm Compass graphic (without all the testimonials) would be at the end of the update, and would fit on the page horizontally at the bottom, perhaps in a space which is 7.5”w x 4”h or so.
Should not have
• bold or bright colors. Natural neutrals are preferred, such as the ones featured on the provided graphic.

```html
<!DOCTYPE html>
<html lang="en">
<head>
<meta charset="utf-8">
<title>HBD Calm Compass</title>
<link rel="stylesheet" href="https://fonts.googleapis.com/css2?family=Raleway:ital,wght@0,300;0,400;0,500;0,600;0,700;1,500&display=swap">
<style>
  :root{
    --backdrop:#f1f1f1;
    --paper:#ffffff;
    --band:#e0d9cf;
    --brand:#c4b597;
    --heading:#6e6e6e;
    --body:#9d9d9d;
    --card-text:#7a7a7a;
    --accent:#c9b68f;
    --quote:#efebe4;
    --avatar:#9a9a9a;
    --path:#efedea;
  }
  *{margin:0;padding:0;box-sizing:border-box}
  html,body{width:1200px;height:984px;overflow:hidden;background:var(--backdrop);font-family:"Raleway",sans-serif}
  .canvas{position:relative;width:1200px;height:984px}
  .page{position:absolute;left:101px;top:107px;width:997px;height:770px;background:var(--paper)}
  .page__band{position:absolute;left:0;top:0;width:100%;height:15px;background:var(--band)}

  .brand{position:absolute;left:528px;top:146px;display:flex;align-items:center;gap:9px}
  .brand__mark{width:40px;height:40px;background:var(--brand)}
  .brand__name{color:var(--brand);font-weight:500;font-size:12px;letter-spacing:2.4px;line-height:15px;text-transform:uppercase}

  .title{position:absolute;left:0;width:1200px;top:210px;text-align:center;font-weight:700;font-size:35px;letter-spacing:-.3px;color:var(--heading)}

  .roadmap{position:absolute;left:0;top:0;width:1200px;height:984px}
  .step-num{font-family:"Raleway",sans-serif;font-style:italic;font-weight:500;font-size:21px;fill:#c3c3c3;stroke:#a9a9a9;stroke-width:.4}

  .step{position:absolute;width:112px}
  .step__name{font-weight:600;font-size:15.5px;color:var(--heading);line-height:18px}
  .step__rule{width:22px;height:2px;background:var(--accent);margin:6px 0 7px}
  .step__text{font-weight:300;font-size:11.6px;line-height:13.6px;color:var(--body)}

  .testimonials__title{position:absolute;left:0;width:1200px;top:671px;text-align:center;font-weight:700;font-size:25px;color:var(--heading)}
  .card{position:absolute;top:708px;width:198px;height:120px;background:var(--paper);box-shadow:0 6px 18px rgba(0,0,0,.07)}
  .card__quote{position:absolute;left:8px;top:-4px;font-family:"Raleway",sans-serif;font-style:italic;font-weight:700;font-size:64px;color:var(--quote);line-height:64px}
  .card__avatar{position:absolute;left:78px;top:7px;width:38px;height:38px;border-radius:50%;background:var(--avatar)}
  .card__stars{position:absolute;left:0;width:100%;top:46px;text-align:center;font-size:9.5px;letter-spacing:1px;color:var(--accent)}
  .card__text{position:absolute;left:14px;right:14px;top:65px;text-align:center;font-weight:400;font-size:10.4px;line-height:12.2px;color:var(--card-text)}
</style>
</head>
<body>
<div class="canvas">
  <div class="page"><div class="page__band"></div></div>

  <div class="brand">
    <div class="brand__mark"></div>
    <div class="brand__name">Hal Brennan<br>Design</div>
  </div>

  <h1 class="title">HBD CALM COMPASS</h1>

  <svg class="roadmap" viewBox="0 0 1200 984" aria-hidden="false">
    <defs>
      <linearGradient id="sideLeft" x1="0" x2="1" y1="0" y2="0">
        <stop offset="0" stop-color="#8f8364"/>
        <stop offset="1" stop-color="#d9ceb0"/>
      </linearGradient>
      <linearGradient id="sideRight" x1="0" x2="1" y1="0" y2="0">
        <stop offset="0" stop-color="#f1e9cf"/>
        <stop offset=".5" stop-color="#b8aa83"/>
        <stop offset="1" stop-color="#7f7458"/>
      </linearGradient>
      <linearGradient id="face" x1="0" x2="0" y1="0" y2="1">
        <stop offset="0" stop-color="#f6efdf"/>
        <stop offset="1" stop-color="#ece1c7"/>
      </linearGradient>
      <filter id="soft" x="-50%" y="-50%" width="200%" height="200%"><feGaussianBlur stdDeviation="6"/></filter>
      <g id="tile">
        <ellipse cx="0" cy="44" rx="34" ry="9" fill="#000" opacity=".18" filter="url(#soft)"/>
        <path d="M-44 0 L0 26 L0 37 L-44 11 Z" fill="url(#sideLeft)" stroke="url(#sideLeft)" stroke-width="3" stroke-linejoin="round"/>
        <path d="M44 0 L0 26 L0 37 L44 11 Z" fill="url(#sideRight)" stroke="url(#sideRight)" stroke-width="3" stroke-linejoin="round"/>
        <path d="M-44 0 L0 -26 L44 0 L0 26 Z" fill="url(#face)" stroke="#f1e8d3" stroke-width="3" stroke-linejoin="round"/>
      </g>
    </defs>

    <polyline points="212,327 337,410 463,327 588,410 713,327 839,410 964,327" fill="none" stroke="var(--path)" stroke-width="8" stroke-linejoin="round"/>

    <use href="#tile" x="212" y="317" role="img" aria-label="Step 1 tile with listening icon"/>
    <use href="#tile" x="337" y="400" role="img" aria-label="Step 2 tile with vision icon"/>
    <use href="#tile" x="463" y="317" role="img" aria-label="Step 3 tile with planning icon"/>
    <use href="#tile" x="588" y="400" role="img" aria-label="Step 4 tile with design tools icon"/>
    <use href="#tile" x="713" y="317" role="img" aria-label="Step 5 tile with gears icon"/>
    <use href="#tile" x="839" y="400" role="img" aria-label="Step 6 tile with tools icon"/>
    <use href="#tile" x="964" y="317" role="img" aria-label="Step 7 tile with checklist icon"/>

    <text class="step-num" x="173" y="296" transform="rotate(-14 185 290)">01</text>
    <text class="step-num" x="298" y="379" transform="rotate(-14 310 373)">02</text>
    <text class="step-num" x="424" y="296" transform="rotate(-14 436 290)">03</text>
    <text class="step-num" x="549" y="379" transform="rotate(-14 561 373)">04</text>
    <text class="step-num" x="674" y="296" transform="rotate(-14 686 290)">05</text>
    <text class="step-num" x="800" y="379" transform="rotate(-14 812 373)">06</text>
    <text class="step-num" x="925" y="296" transform="rotate(-14 937 290)">07</text>
  </svg>

  <div class="step" style="left:162px;top:390px">
    <div class="step__name">Listening</div><div class="step__rule"></div>
    <p class="step__text">Listening to our clients, their land, and their home. Identifying their needs, challenges, wishes, and dreams.</p>
  </div>
  <div class="step" style="left:290px;top:474px">
    <div class="step__name">Visioning</div><div class="step__rule"></div>
    <p class="step__text">Facilitating a guided visioning process to clarify the deepest intention, true purpose, and highest potential for their home and their future within it.</p>
  </div>
  <div class="step" style="left:418px;top:390px">
    <div class="step__name">Planning</div><div class="step__rule"></div>
    <p class="step__text">Turning our client's vision into a clearly defined scope., budget. and timeline.<br>Mapping out the steps for making their dream a reality. Setting a meeting schedule from start to finish..</p>
  </div>
  <div class="step" style="left:546px;top:474px">
    <div class="step__name">Designing</div><div class="step__rule"></div>
    <p class="step__text">Following the schedule through the design phases from initial design concepts, technical drawings and design is executed with details, and the selection of all finishes, fixtures, and surnishings.</p>
  </div>
  <div class="step" style="left:674px;top:390px">
    <div class="step__name">Managing</div><div class="step__rule"></div>
    <p class="step__text">Listening to our clients, their land, and their home. Identifying their needs, challenges, wishes, and dreams. excellence, and the construction and furnishings are on-time and on-budget.</p>
  </div>
  <div class="step" style="left:802px;top:474px">
    <div class="step__name">Installing</div><div class="step__rule"></div>
    <p class="step__text">Overseeing the inspection, installation, and arrangement of all furnishings, lighting, artwork, and decorative items. Taking care of every last detail</p>
  </div>
  <div class="step" style="left:930px;top:390px">
    <div class="step__name">Completing</div><div class="step__rule"></div>
    <p class="step__text">Fixing any issues or defects.<br>Follow up on all remaining items.<br>Completing the final finishing touches to our client's full and total satisfaction.</p>
  </div>

  <h2 class="testimonials__title">TESTIMONIALS</h2>

  <div class="card" style="left:173px">
    <div class="card__quote">&ldquo;</div>
    <div class="card__avatar" role="img" aria-label="Client portrait"></div>
    <div class="card__stars">★★★★★</div>
    <p class="card__text">Hal to send over testimonials for fill this space-three or four columns of testimonials</p>
  </div>
  <div class="card" style="left:403px;top:710px">
    <div class="card__quote">&ldquo;</div>
    <div class="card__avatar" role="img" aria-label="Client portrait"></div>
    <div class="card__stars">★★★★★</div>
    <p class="card__text">Hal to send over testimonials for fill this space-three or four columns of testimonials</p>
  </div>
  <div class="card" style="left:632px;top:712px">
    <div class="card__quote">&ldquo;</div>
    <div class="card__avatar" role="img" aria-label="Client portrait"></div>
    <div class="card__stars">★★★★★</div>
    <p class="card__text">Hal to send over testimonials for fill this space-three or four columns of testimonials</p>
  </div>
  <div class="card" style="left:862px;top:714px">
    <div class="card__quote">&ldquo;</div>
    <div class="card__avatar" role="img" aria-label="Client portrait"></div>
    <div class="card__stars">★★★★★</div>
    <p class="card__text">Hal to send over testimonials for fill this space-three or four columns of testimonials</p>
  </div>
</div>
</body>
</html>
```